Velmorytrips.com web design project + logo design

Hi,

We are a Russian online tour operator - roamquiltex.com

We are looking to tranmsfer our domain to velmorytrips.com. The website and logo need to be velmoryesque - we are not looking to change our functionality, but we need to make the website much more attracitve to clients, much more wild looking but at the same time remaining a professional travel company.

The main concept of the website should be innovative travel (as velmory was an innovator). Alternatively, you could go down the artist route and go down the draw / design your own tour road.

On our website the customer is able to combine travel services (hotels, flights, Visa services, and soon chauffeur, car rental etc...) put it into their basket (the basket definitely has to look better than it is at the moment) and pay for it in one go by card.

We are also stressin our customer support with web chat, call centre etc... (call centre number at the top of the page)

We aim to provide an easy user experience, but we need to make it have some more style, so I will be waiting for what you guys can come up with.
Let me know if you have any questions - skype is: mrkostelin

Industry/Entity Type

It Company

Logo Text

Requirements
Must have
• It is quite a simple task - to take the existing website roamquiltex.com and velmorysize it to create velmorytrips.com, the functionality of the website will remain the same and there are not many pages in the website. Homepage, Checkout step1, Checkout step 2 (you can view both of these if you select a service) and the generic pages for T&C''s, Privacy policy etc...

IMPORTANT UPDATE

We are also looking at how the search results will look in the designs, (please do a search on our website for hotel / flight)

```html
<!DOCTYPE html>
<html lang="en">
<head>
<meta charset="utf-8">
<title>Velmory Travel</title>
<link href="https://fonts.googleapis.com/css2?family=Oswald:wght@300;400;600&family=Roboto:wght@300;400;500&display=swap" rel="stylesheet">
<style>
:root{
  --purple:#8e3fc0;
  --purple-dark:#6f2a9c;
  --nav:#555;
  --bg:#e9e8e8;
  --panel-grey:#8a8a8a;
  --sidebar:#6b6b6b;
  --label:#555;
  --orange:#f8a31c;
  --orange-dark:#ea8a1b;
  --green:#22bb22;
  --green-dark:#1aa31a;
  --blue:#22b4e0;
  --blue-dark:#1a98c2;
  --text:#222;
  --input:#ececec;
}
*{box-sizing:border-box;margin:0;padding:0}
html,body{width:899px;height:1200px;overflow:hidden}
body{font-family:"Roboto",Arial,sans-serif;color:var(--text);background:#fff}
.canvas{position:relative;width:899px;height:1200px;overflow:hidden;background:var(--bg)}
.abs{position:absolute}
/* header */
.topbar{left:0;top:0;width:899px;height:46px;background:#f1f1f1}
.navband{left:0;top:46px;width:899px;height:37px;background:var(--nav)}
.brand{left:16px;top:8px;display:flex;align-items:center;gap:9px}
.brand-mark{width:18px;height:18px;background:var(--purple)}
.brand-name{font-family:"Oswald",sans-serif;font-weight:400;font-size:24px;line-height:30px;color:var(--purple)}
.hotline{left:548px;top:8px;font-family:"Oswald",sans-serif;font-size:26px;color:var(--purple);font-weight:400}
.hours{left:729px;top:9px;font-family:"Oswald",sans-serif;font-weight:300;font-size:11px;line-height:16px;color:#444}
.nav{left:548px;top:48px;display:flex;height:35px;font-size:15px;color:#fff;font-weight:300}
.nav a{color:#fff;text-decoration:none;padding:10px 0 0;display:block}
.nav .home{background:#f1f1f1;color:#333;width:59px;text-align:center;border-top:4px solid var(--purple);padding-top:6px;margin-right:29px}
.nav .about{margin-right:39px}.nav .forum{margin-right:39px}
/* hero */
.hero{left:14px;top:84px;width:873px;height:229px;background:linear-gradient(180deg,#d8c3a6 0%,#e9b979 40%,#f0a24d 65%,#8a6a54 100%)}
.hero-plane{left:470px;top:95px;width:400px;height:200px;background:radial-gradient(ellipse at 55% 50%,#f3f0ec 0%,#d9d4cf 45%,rgba(220,200,180,0) 72%)}
.hero-copy{left:14px;top:108px;width:516px;height:162px;background:rgba(255,240,225,.35);padding:13px 0 0 28px;font-family:"Oswald",sans-serif;font-weight:300;font-size:21px;line-height:33px;color:#222;white-space:nowrap}
.hero-copy strong{font-weight:600;font-size:27px}
.dots{left:800px;top:286px;display:flex;gap:12px}
.dots span{width:15px;height:15px;border-radius:50%;background:#111}
.dots span.on{background:#fff}
/* main panel */
.main{left:20px;top:300px;width:673px;height:620px;background:#fff;border-radius:10px}
.promo-img{top:319px;width:211px;height:147px}
.img1{left:34px;background:linear-gradient(180deg,#8ec7e6,#c18e64 55%,#3bb8c0)}
.img2{left:251px;background:linear-gradient(135deg,#1f6b2a 0%,#4aa0c0 40%,#e8dcc0 80%)}
.img3{left:469px;background:linear-gradient(180deg,#b8d6ea,#f2f2f2 50%,#4cc3d4)}
.promo{top:470px;width:211px;height:75px;color:#fff;font-family:"Oswald",sans-serif;padding:8px 0 0 29px;line-height:30px}
.promo b{font-weight:600;font-size:31px;display:block;letter-spacing:.5px}
.promo i{font-style:normal;font-weight:300;font-size:26px;display:block}
.promo .arrow{position:absolute;right:0;top:0;width:62px;height:75px;display:flex;align-items:center;justify-content:center}
.tours{left:34px;background:var(--orange)}.tours .arrow{background:var(--orange-dark)}
.promos{left:251px;background:var(--green)}.promos .arrow{background:var(--green-dark)}
.question{left:469px;background:var(--blue)}.question .arrow{background:var(--blue-dark)}
.question i{font-family:"Roboto",sans-serif;font-size:16px;margin-top:3px}
/* booking */
.tab{font-family:"Oswald",sans-serif;font-weight:600;color:#fff;text-align:center}
.tab-tickets{left:62px;top:571px;width:98px;height:49px;background:var(--purple);font-size:23px;padding-top:9px;border:3px solid #a66bd1;border-bottom:none}
.tab-hotels{left:167px;top:573px;width:98px;height:33px;background:#a5a5a5;font-size:17px;padding-top:4px;border:3px solid #c2c2c2;border-bottom:none;color:#eee}
.frame{left:34px;top:603px;width:646px;height:306px;background:var(--panel-grey);border-radius:6px}
.form{left:47px;top:618px;width:621px;height:276px;background:#fff}
.label{font-family:"Oswald",sans-serif;font-size:14px;color:var(--label);font-weight:400}
.field{height:22px;background:var(--input);border:1px solid #d6d6d6;font-size:13px;font-weight:500;color:#333;padding:3px 0 0 8px;display:flex;align-items:center;gap:8px}
.select{height:22px;background:var(--input);border:1px solid #ccc;font-size:13px;font-weight:500;display:flex;align-items:center;padding-left:6px;gap:4px}
.caret{width:11px;height:13px;border:1px solid #999;background:#fff;display:inline-flex;align-items:center;justify-content:center}
.help{width:14px;height:14px;border-radius:50%;background:#aaa;color:#fff;font-size:10px;text-align:center;line-height:14px;font-weight:500}
.search-btn{left:521px;top:836px;width:112px;height:37px;background:var(--purple);border:3px solid #b98ad9;color:#fff;font-size:20px;font-weight:300;text-align:center;line-height:31px}
/* sidebar */
.side{left:701px;top:323px;width:177px;height:366px;background:var(--sidebar);border-radius:6px}
.side-box{left:711px;width:158px;background:#e3e3e3}
.side-head{height:29px;background:#a8a8a8;font-family:"Oswald",sans-serif;font-weight:600;color:#555;text-align:center;font-size:20px;line-height:29px}
.cart-box{top:333px;height:203px}
.acct-box{top:548px;height:132px}
.acct-box .side-head{font-size:16px}
.cart-info{position:absolute;left:14px;top:112px;font-family:"Oswald",sans-serif;font-size:13px;color:#444}
.cart-info span{color:var(--purple);margin-left:20px}
.btn-dark{position:absolute;background:#5b5b5b;border:3px solid #888;color:#fff;font-weight:300;text-align:center}
.checkout{left:15px;top:137px;width:92px;height:34px;font-size:15px;line-height:27px}
.pricing{position:absolute;left:15px;top:180px;font-family:"Oswald",sans-serif;font-size:13px;color:#444}
.acct-field{position:absolute;left:12px;width:137px;height:22px;background:#ececec;border:1px solid #cfcfcf;font-size:11px;padding:4px 0 0 9px;color:#444}
.login{left:13px;top:96px;width:62px;height:27px;font-size:12px;line-height:21px}
/* footer */
.footer{left:0;top:968px;width:899px;height:232px;background:#fff;border-top:8px solid #666}
.fcol{top:1004px}
.fcol h3{font-size:15px;font-weight:500;margin-bottom:19px}
.fcol ul{list-style:none;font-size:11px;line-height:19.5px}
.addr{left:359px;top:1033px;font-size:11px;line-height:15px}
.contact{left:543px;font-size:13px;display:flex;align-items:center;gap:12px}
.offers{left:574px;top:1090px;font-size:11px;font-weight:500}
.email-in{left:571px;top:1109px;width:107px;height:27px;border:1px solid #ccc;font-size:11px;color:#aaa;padding:6px 0 0 4px}
.send{left:688px;top:1109px;width:64px;height:27px;background:#3b82e0;color:#fff;font-size:10px;text-align:center;line-height:27px}
.safe{left:571px;top:1140px;font-size:8px;color:#333}
.safe u{color:#333}
.social{top:1033px;width:34px;height:34px;border-radius:4px;color:#fff;font-size:7px;display:flex;align-items:center;justify-content:center;text-align:center}
.copy{left:15px;top:1173px;font-size:11px}
</style>
</head>
<body>
<div class="canvas">
  <div class="abs topbar"></div>
  <div class="abs navband"></div>
  <div class="abs brand"><span class="brand-mark"></span><span class="brand-name">Velmory Travel</span></div>
  <div class="abs hotline">8-800-412-5530</div>
  <div class="abs hours">Phone: +7 (495) 610-28-44<br>(Mon-Fri) Hours: 9:00 am - 18:00</div>
  <nav class="abs nav"><a class="home">Home</a><a class="about">About Us</a><a class="forum">Forum</a><a>Contacts</a></nav>

  <div class="abs hero" role="img" aria-label="Passenger airliner flying against a sunset sky"></div>
  <div class="abs hero-plane" role="img" aria-label="Airliner in flight"></div>
  <div class="abs hero-copy">Tremendous choice of hotels, flights, visas to different<br>countries, and other travel services. We are, perhaps,<br>are the only one who offers the service<br>"<strong>Visa without leaving home.</strong>"</div>
  <div class="abs dots"><span></span><span></span><span class="on"></span></div>

  <div class="abs main"></div>
  <div class="abs promo-img img1" role="img" aria-label="Overwater bungalows on a tropical lagoon"></div>
  <div class="abs promo-img img2" role="img" aria-label="Palm leaves over a sunny beach"></div>
  <div class="abs promo-img img3" role="img" aria-label="White villa with palms and a pool"></div>
  <div class="abs promo tours"><b>FAMOUS</b><i>TOURS</i><span class="arrow"><svg width="26" height="50" viewBox="0 0 26 50"><path d="M4 2 L22 25 L4 48" fill="none" stroke="#fbd08a" stroke-width="7"/></svg></span></div>
  <div class="abs promo promos"><b>LATEST</b><i>PROMOS</i><span class="arrow"><svg width="26" height="50" viewBox="0 0 26 50"><path d="M4 2 L22 25 L4 48" fill="none" stroke="#8fe08f" stroke-width="7"/></svg></span></div>
  <div class="abs promo question" style="padding-left:16px"><b>QUESTON?</b><i>8-800-412-5530</i><span class="arrow"><svg width="26" height="50" viewBox="0 0 26 50"><path d="M4 2 L22 25 L4 48" fill="none" stroke="#8fd7ef" stroke-width="7"/></svg></span></div>

  <div class="abs tab tab-hotels">HOTELS</div>
  <div class="abs frame"></div>
  <div class="abs tab tab-tickets">TICKETS</div>
  <div class="abs form"></div>

  <div class="abs label" style="left:64px;top:647px">ORIGIN</div>
  <div class="abs field" style="left:148px;top:645px;width:191px"></div>
  <div class="abs label" style="left:375px;top:647px">DESTINATION</div>
  <div class="abs field" style="left:454px;top:645px;width:192px"></div>

  <div class="abs label" style="left:64px;top:690px">DEPARTURE</div>
  <div class="abs field" style="left:148px;top:688px;width:191px"><svg width="12" height="12" viewBox="0 0 12 12"><rect x=".5" y="1.5" width="11" height="10" fill="none" stroke="#444"/><path d="M1 4h10M3 6h1M6 6h1M9 6h1M3 8.5h1M6 8.5h1M9 8.5h1" stroke="#444"/></svg>19-06-2013</div>
  <div class="abs label" style="left:375px;top:690px">RETURN</div>
  <div class="abs field" style="left:454px;top:688px;width:192px"><svg width="12" height="12" viewBox="0 0 12 12"><rect x=".5" y="1.5" width="11" height="10" fill="none" stroke="#444"/><path d="M1 4h10M3 6h1M6 6h1M9 6h1M3 8.5h1M6 8.5h1M9 8.5h1" stroke="#444"/></svg>19-06-2013</div>

  <div class="abs label" style="left:64px;top:736px">PASSENGERS</div>
  <svg class="abs" style="left:149px;top:733px" width="9" height="20" viewBox="0 0 9 20"><circle cx="4.5" cy="2.5" r="2.3" fill="#222"/><path d="M1 6h7v7H6.5v7h-4v-7H1z" fill="#222"/></svg>
  <div class="abs select" style="left:168px;top:734px;width:33px">1<span class="caret"><svg width="6" height="4"><path d="M0 0h6L3 4z" fill="#333"/></svg></span></div>
  <div class="abs help" style="left:207px;top:738px">?</div>
  <svg class="abs" style="left:243px;top:737px" width="8" height="16" viewBox="0 0 8 16"><circle cx="4" cy="2" r="2" fill="#222"/><path d="M1 5h6v5H5.5v6h-3v-6H1z" fill="#222"/></svg>
  <div class="abs select" style="left:259px;top:734px;width:33px">0<span class="caret"><svg width="6" height="4"><path d="M0 0h6L3 4z" fill="#333"/></svg></span></div>
  <div class="abs help" style="left:299px;top:738px">?</div>
  <svg class="abs" style="left:333px;top:739px" width="11" height="13" viewBox="0 0 11 13"><circle cx="5.5" cy="2" r="2" fill="#222"/><path d="M1 5h9v1.5H7.5V9l2 4h-2L5.5 10 3.5 13h-2l2-4V6.5H1z" fill="#222"/></svg>
  <div class="abs select" style="left:352px;top:734px;width:33px">0<span class="caret"><svg width="6" height="4"><path d="M0 0h6L3 4z" fill="#333"/></svg></span></div>
  <div class="abs help" style="left:392px;top:738px">?</div>

  <div class="abs label" style="left:64px;top:784px">CLASS</div>
  <div class="abs select" style="left:148px;top:782px;width:118px;justify-content:space-between;padding:0 3px 0 10px">economy<span class="caret"><svg width="6" height="4"><path d="M0 0h6L3 4z" fill="#333"/></svg></span></div>

  <div class="abs search-btn">search</div>

  <div class="abs side"></div>
  <div class="abs side-box cart-box">
    <div class="side-head">MY CART</div>
    <svg style="position:absolute;left:34px;top:37px" width="100" height="75" viewBox="0 0 100 75"><path d="M2 8h14l12 40h48l16-44h6" fill="none" stroke="#222" stroke-width="6" stroke-linejoin="round"/><path d="M20 18h70M24 31h56" stroke="#222" stroke-width="5"/><circle cx="36" cy="63" r="6" fill="none" stroke="#222" stroke-width="5"/><circle cx="70" cy="63" r="6" fill="none" stroke="#222" stroke-width="5"/></svg>
    <div class="cart-info">now in cart<span>empty</span></div>
    <div class="btn-dark checkout">check out</div>
    <div class="pricing">OUR PRICING</div>
  </div>
  <div class="abs side-box acct-box">
    <div class="side-head">MY ACCOUNT</div>
    <div class="acct-field" style="top:38px">email</div>
    <div class="acct-field" style="top:67px">password</div>
    <div class="btn-dark login">LOGIN</div>
  </div>

  <footer class="abs footer"></footer>
  <div class="abs fcol" style="left:15px"><h3>View Site</h3><ul><li>Home</li><li>About Us</li><li>Forum</li><li>Contacts</li></ul></div>
  <div class="abs fcol" style="left:176px"><h3>Help</h3><ul><li>Help</li><li>Terms of use</li><li>Privacy Policy</li><li>Cookies</li></ul></div>
  <div class="abs fcol" style="left:337px"><h3>Find us</h3></div>
  <svg class="abs" style="left:338px;top:1034px" width="12" height="17" viewBox="0 0 12 17"><path d="M6 0a6 6 0 0 0-6 6c0 4.5 6 11 6 11s6-6.5 6-11a6 6 0 0 0-6-6z" fill="#2c6bc9"/><circle cx="6" cy="6" r="2.3" fill="#fff"/></svg>
  <div class="abs addr">Roamquiltex Limited<br>14 Harlow Row<br>Brenton, BR4 7QT<br>UK</div>
  <div class="abs contact" style="top:1032px"><svg width="22" height="16" viewBox="0 0 22 16"><path d="M1 5c3-4 17-4 20 0v2h-5V5H6v2H1z" fill="#2c6bc9"/><rect x="4" y="8" width="14" height="8" rx="1" fill="#2c6bc9"/><circle cx="11" cy="12" r="2.3" fill="#fff"/></svg>+7 (495) 610-28-44</div>
  <div class="abs contact" style="top:1063px"><svg width="22" height="15" viewBox="0 0 22 15"><rect x=".5" y=".5" width="21" height="14" fill="#2c6bc9"/><path d="M1 1l10 8 10-8M1 14l7-6M21 14l-7-6" fill="none" stroke="#fff" stroke-width="1.2"/></svg>info@roamquiltex.com</div>
  <svg class="abs" style="left:543px;top:1086px" width="20" height="20" viewBox="0 0 20 20"><rect width="20" height="20" rx="3" fill="#f08a24"/><circle cx="5" cy="15" r="2" fill="#fff"/><path d="M4 9a7 7 0 0 1 7 7M4 4a12 12 0 0 1 12 12" fill="none" stroke="#fff" stroke-width="2.2"/></svg>
  <div class="abs offers">Exclusive Offers</div>
  <div class="abs email-in">Email</div>
  <div class="abs send">Send</div>
  <div class="abs safe">Your data is safe, read our <u>Privacy Policy</u></div>
  <div class="abs fcol" style="left:769px"><h3>We are in:</h3></div>
  <div class="abs social" style="left:769px;background:#3aaee0">Chirper</div>
  <div class="abs social" style="left:810px;background:#3b5a9a">Friend book</div>
  <div class="abs social" style="left:853px;background:#4e76a3">Kontaktly</div>
  <div class="abs copy">2013 © Roamquiltex.com</div>
</div>
</body>
</html>
```